Meditation for IVF and infertility

I need a flyer inviting IVF patients to join my Meditation class, I would like to offer free meditation to ivf women and for couples this class is free every Thursday night at 5 pm
2437 west harlow ave suite K Santa Barbara Ca 93142
quillbrook-stillness.com for more details

```html
<!DOCTYPE html>
<html lang="en">
<head>
<meta charset="utf-8">
<title>Quillbrook Stillness – Free Meditation Classes</title>
<link rel="stylesheet" href="https://fonts.googleapis.com/css2?family=Roboto+Condensed:wght@300;400;700&family=Roboto:wght@400;700&display=swap">
<style>
  :root {
    --paper: #ffffff;
    --ink: #1e1e1e;
    --ink-soft: #5d5d5d;
    --logo-grey: #6f6f6f;
    --band-light: #d9d9d9;
    --band-mid: #a9a9a9;
    --band-dark: #4a4a4a;
    --box-dark: #2b2b2b;
    --box-darker: #151515;
    --text-on-dark: #ffffff;
    --text-on-dark-soft: #c9c9c9;
    --photo-light: #f4f2ef;
    --photo-mid: #e2dcd6;
    --photo-skin: #cdb3a0;
    --footer-tint: #ececec;
  }
  * { margin: 0; padding: 0; box-sizing: border-box; }
  html, body {
    width: 900px; height: 1200px; overflow: hidden;
    background: var(--paper);
    font-family: "Roboto", Arial, sans-serif;
  }
  .flyer {
    position: relative; width: 900px; height: 1200px;
    background: var(--paper); overflow: hidden;
  }
  .brand {
    position: absolute; left: 70px; top: 100px;
    font-family: "Roboto Condensed", Arial, sans-serif;
    font-weight: 300; color: var(--logo-grey);
    line-height: 1;
  }
  .brand-name { font-size: 86px; letter-spacing: 1px; display: block; }
  .brand-sub { font-size: 46px; letter-spacing: 3px; display: block; margin: 10px 0 0 120px; }
  .offer-band {
    position: absolute; left: 0; top: 330px; width: 900px; height: 480px;
    background: linear-gradient(90deg, var(--band-light) 0%, var(--band-mid) 45%, var(--band-dark) 100%);
  }
  .band-accent {
    position: absolute; right: 0; top: 380px; width: 140px; height: 390px;
    background: var(--box-darker);
  }
  .portrait {
    position: absolute; left: 440px; top: 60px; width: 400px; height: 1010px;
    background: radial-gradient(ellipse at 55% 35%, var(--photo-skin) 0%, var(--photo-mid) 30%, var(--photo-light) 70%);
    border-radius: 180px 180px 40px 40px;
  }
  .free-box {
    position: absolute; left: 30px; top: 395px; width: 450px; height: 185px;
    background: linear-gradient(180deg, var(--box-dark), var(--box-darker));
    color: var(--text-on-dark);
    font-family: "Roboto Condensed", Arial, sans-serif;
    padding: 28px 0 0 60px;
  }
  .free-title { font-size: 92px; font-weight: 700; line-height: 1; letter-spacing: 2px; }
  .free-note {
    margin-top: 14px; font-size: 19px; line-height: 1.3;
    color: var(--text-on-dark-soft); text-transform: uppercase; letter-spacing: 1px;
  }
  .class-box {
    position: absolute; left: 30px; top: 600px; width: 470px; height: 210px;
    background: linear-gradient(180deg, #3a3a3a, var(--box-darker));
    color: var(--text-on-dark);
    font-family: "Roboto Condensed", Arial, sans-serif;
    padding: 30px 0 0 60px; text-transform: uppercase; line-height: 1.02;
  }
  .class-line-strong { font-size: 64px; font-weight: 700; display: block; }
  .class-line-light { font-size: 56px; font-weight: 300; display: block; color: var(--text-on-dark-soft); }
  .class-line-place { font-size: 50px; font-weight: 700; display: block; }
  .footer {
    position: absolute; left: 0; top: 880px; width: 900px; height: 320px;
    background: linear-gradient(180deg, var(--paper) 0%, var(--footer-tint) 100%);
  }
  .contact {
    position: absolute; left: 0; top: 915px; width: 900px; text-align: center; color: var(--ink);
  }
  .phone {
    display: inline-flex; align-items: center; gap: 18px;
    font-family: "Roboto Condensed", Arial, sans-serif;
    font-size: 62px; font-weight: 700; letter-spacing: 1px;
  }
  .phone svg { width: 44px; height: 44px; }
  .address { margin-top: 18px; font-size: 24px; font-weight: 700; }
  .website { margin-top: 32px; font-size: 22px; letter-spacing: 8px; color: var(--ink-soft); }
</style>
</head>
<body>
<main class="flyer">
  <div class="footer"></div>
  <div class="offer-band"></div>
  <div class="band-accent"></div>
  <div class="portrait" role="img" aria-label="Photograph of a smiling pregnant woman in a white shirt holding her belly"></div>

  <header class="brand">
    <span class="brand-name">Quillbrook</span>
    <span class="brand-sub">Stillness</span>
  </header>

  <section class="free-box">
    <div class="free-title">FREE</div>
    <p class="free-note">Classes for couple in every<br>Thursday night at 5 pm</p>
  </section>

  <section class="class-box">
    <span class="class-line-strong">Meditation</span>
    <span class="class-line-light">Classes</span>
    <span class="class-line-place">in Montecito</span>
  </section>

  <section class="contact">
    <div class="phone">
      <svg viewBox="0 0 24 24" aria-hidden="true"><path fill="currentColor" d="M6.6 10.8a15.1 15.1 0 0 0 6.6 6.6l2.2-2.2c.3-.3.7-.4 1-.2 1.1.4 2.3.6 3.6.6.6 0 1 .4 1 1V20c0 .6-.4 1-1 1A17 17 0 0 1 3 4c0-.6.4-1 1-1h3.5c.6 0 1 .4 1 1 0 1.3.2 2.5.6 3.6.1.3 0 .7-.2 1z"/></svg>
      (707) 555-0148
    </div>
    <p class="address">2437 west harlow ave suite K Santa Barbara Ca 93142</p>
    <p class="website">www.quillbrook-stillness.com</p>
  </section>
</main>
</body>
</html>
```